Business Card - Rebranding for Consulting Firm

We are renaming and rebranding our consulting firm and need to raise the level of quality of our cards as part of that effort. We consult to leading high tech, life science and other innovation sector companies.

Need a two-sided business card design.

Side 1: (a) Company logo (b) tag line: Elevate the People Behind Your Plan (c) Name (d) Title (e) Phone 1: Office (f) Phone 2: Mobile (g) email: person@HollowmereAdvisory.com

Side 2: Two lines of text: (a) Markets Shift Quickly. Teams Must Adapt. People Deliver Results. (b) We help you master every one.

Target Market(s)

Business and human resources executives and senior managers

Industry/Entity Type

Management Consulting

Contact Information for Business Card

Font styles to use
Sans Serif

Requirements
Must have
• clean, not too busy, but with a bit of creativity. Stick to the colors used in the attached logo
• appeal to high tech, life science companies
Nice to have
• prefer white background

```html
<!DOCTYPE html>
<html lang="en">
<head>
<meta charset="utf-8">
<title>Hollowmere Advisory – Double-Sided Business Card</title>
<link href="https://fonts.googleapis.com/css2?family=Roboto:wght@400;500;700&family=Roboto+Condensed:wght@500&display=swap" rel="stylesheet">
<style>
  :root {
    --brand-blue: #0d67a3;
    --brand-sky: #0a8fcf;
    --brand-steel: #6a8393;
    --text-grey: #6b7378;
    --card-white: #f7f7f7;
    --canvas-bg: #e9eef1;
  }
  * { margin: 0; padding: 0; box-sizing: border-box; }
  html, body {
    width: 1200px; height: 1200px; overflow: hidden;
    background: var(--canvas-bg);
    font-family: "Roboto", Arial, sans-serif;
  }
  .sheet {
    width: 1200px; height: 1200px;
    display: flex; align-items: center; justify-content: center; gap: 40px;
  }
  .card {
    position: relative;
    width: 560px; height: 340px;
    background: var(--card-white);
  }
  /* Front */
  .brand {
    position: absolute; left: 236px; top: 64px; width: 290px; text-align: right;
  }
  .brand-name {
    display: block;
    font-weight: 500; font-size: 36px; letter-spacing: -0.5px;
    color: var(--brand-blue); line-height: 1;
  }
  .brand-sub {
    display: block; margin-top: 7px;
    font-weight: 500; font-size: 11px; letter-spacing: 6.2px;
    margin-right: -6.2px;
    color: var(--brand-blue);
  }
  .brand-rule {
    position: absolute; left: 238px; top: 145px; width: 288px; height: 4px;
    background: linear-gradient(to right, var(--brand-steel) 0 30%, var(--brand-sky) 30% 100%);
  }
  .tagline {
    position: absolute; right: 34px; top: 152px;
    font-family: "Roboto Condensed", "Arial Narrow", sans-serif;
    font-weight: 500; font-size: 12.5px; color: var(--brand-blue);
  }
  .contact { position: absolute; left: 39px; top: 210px; }
  .person-name {
    font-weight: 700; font-size: 17px; color: var(--brand-blue); letter-spacing: 0.2px;
  }
  .person-title {
    font-size: 13px; color: var(--text-grey); margin-top: 2px;
  }
  .phones { margin-top: 16px; font-size: 14px; color: var(--text-grey); }
  .phones .mobile { color: var(--brand-blue); }
  .email { font-size: 14px; color: var(--text-grey); margin-top: 3px; }
  /* Back */
  .statement {
    position: absolute; left: 52px; top: 176px;
    display: flex; align-items: center; gap: 12px;
  }
  .statement-mark { width: 22px; height: 22px; background: var(--brand-blue); flex: none; }
  .statement-text { font-size: 12.6px; line-height: 20px; color: var(--brand-blue); }
</style>
</head>
<body>
<main class="sheet">
  <section class="card card-front" aria-label="Business card front">
    <div class="brand">
      <span class="brand-name">Hollowmere</span>
      <span class="brand-sub">ADVISORY LLC</span>
    </div>
    <div class="brand-rule"></div>
    <p class="tagline">Elevate the People Behind Your Plan</p>
    <div class="contact">
      <p class="person-name">MARCO VALENTINI</p>
      <p class="person-title">FOUNDER &amp; CEO</p>
      <p class="phones">+66 2555 0147 &nbsp;/&nbsp; <span class="mobile">+668 5550 1928</span></p>
      <p class="email">person@HollowmereAdvisory.com</p>
    </div>
  </section>

  <section class="card card-back" aria-label="Business card back">
    <div class="statement">
      <span class="statement-mark"></span>
      <p class="statement-text">Markets Shift Quickly. Teams Must Adapt. People Deliver Results.<br>We help you master every one.</p>
    </div>
  </section>
</main>
</body>
</html>
```